Varko Engineering global website design

Our existing website is www.varkoltd-example.com.tr. The content will be more or less the same, but there will be some differences such as below. We will move to the global address that is www.varkoengineering-example.com.
1. Logo will change (please find the new logo attached)
2. "Projects" section will be presented in a better way
3. We now have 3 companies spread in Greece, Turkey and the Netherlands, so we need to make sure when someone has access from Turkey, the Turkish site opens. When someone gets into the address from Greece, the Greek site will open. English version will open for all other cases.

We have a hosting and URL services already, so if we can just move your design to that infrastructure, it would be the best.

Turkish and English content are attached. Greek content is to follow.

High-quality photos are also attached to be used in banners.

We can remove the "Services" tab that is in the existing website of www.varkoltd-example.com.tr.

Please use the attached PPT files for the "Projects" tab. Please note that this is the most important part of the site.

We can remove the "Research & Development" tab that is in the existing website of www.varkoltd-example.com.tr.

In the "Contact Us" tab, we need to give the info for the 3 companies in Turkey, Greece and Netherlands. The contact details for the Turkey office can be found from www.varkoltd-example.com.tr .
The contact details for the Netherlands office:
Varko Engineering B.V.
Lindehof 52, 9714TK, Oostbroek, The Netherlands
Tel:+31 (0)6 00 00 73 85
e-mail: info@varkoengineering-example.com

The contact details for the Greece office:
Leof. Trigonou 7 & Paronos
Ano Kalyvia, 14590
Athens, Greece
Tel +30 210 0000947

Finally, please also add social media links:
https://twitter.com/VarkoEng
https://www.linkedin.com/in/varko-mühendislik-x7q20419/
https://www.facebook.com/varkoengineering/

Target Market(s)

structural engineering, industrial vibration control

Industry/Entity Type

Structural Engineering

Coding

Coded - Design and coding required

Number of Pages Required

5+ page

Font styles to use
Serif

Requirements
Must have
• Tri-langual concept
Nice to have
• A map with our customers (i.e. dots on Greece, Netherlands, Azerbaijan, Denmark and Turkey)

```html
<!DOCTYPE html>
<html lang="en">
<head>
<meta charset="utf-8">
<title>Varko Engineering – Vibration Solutions</title>
<link rel="stylesheet" href="https://fonts.googleapis.com/css2?family=Lora:ital,wght@0,400;0,700;1,400;1,700&family=Playfair+Display:wght@400;700&display=swap">
<style>
:root{
  --navy:#0c2a6a;
  --navy-deep:#0a2460;
  --orange:#fb8c0a;
  --topbar:#d8dee8;
  --band:#d4dae3;
  --acc-head:#d3dae6;
  --acc-body:#e6ebf4;
  --text:#3a3f48;
  --muted:#5b6270;
  --white:#ffffff;
}
*{box-sizing:border-box;margin:0;padding:0}
html,body{width:1200px;height:2350px;overflow:hidden}
body{position:relative;font-family:"Lora",serif;color:var(--text);background:var(--white)}
.icon{display:inline-block;vertical-align:middle;flex:none}

/* top bar */
.topbar{height:42px;background:var(--topbar);display:flex;align-items:center;padding-left:110px;font-size:12px;color:#2f3540}
.topbar .item{display:flex;align-items:center;gap:9px;white-space:nowrap}
.topbar .address{width:680px}
.topbar .phone{width:140px}

/* header */
.header{height:83px;display:flex;align-items:center;padding:0 110px}
.logo{position:relative;display:inline-block;color:var(--navy)}
.logo .tag{position:absolute;top:-4px;left:30px;font-size:10px;font-style:italic;white-space:nowrap}
.logo .name{font-size:48px;font-weight:400;line-height:1}
.nav{display:flex;gap:26px;margin-left:150px;font-size:13.5px;text-transform:uppercase;color:#2f3540}
.nav .active{color:var(--navy);font-weight:700}
.flags{display:flex;gap:7px;margin-left:auto}
.search{margin-left:14px}

/* hero */
.hero{position:relative;height:455px;background:linear-gradient(120deg,#c97a2a 0%,#9ea9b4 35%,#d9dde0 55%,#6f5a48 80%,#e9ecef 100%);text-align:center;color:var(--white)}
.hero .photo{position:absolute;inset:0}
.hero h1{position:absolute;top:205px;width:100%;font-size:29px;font-weight:700;text-shadow:0 1px 4px rgba(0,0,0,.35)}
.hero .sub{position:absolute;top:250px;width:100%;font-size:15px}
.btn{display:inline-block;background:var(--orange);color:var(--white);border-radius:5px;text-transform:uppercase;text-align:center}
.hero .btn{position:absolute;top:297px;left:522px;width:156px;height:37px;line-height:37px;font-size:15px}
.hero .arrows{position:absolute;top:380px;left:542px;display:flex;gap:12px}
.hero .arrow{width:51px;height:51px;border-radius:50%;background:rgba(255,255,255,.85);display:flex;align-items:center;justify-content:center}

/* newsletter */
.newsletter{height:106px;background:var(--navy);display:flex;align-items:center;padding-left:168px}
.newsletter h2{font-size:28px;font-style:italic;font-weight:700;color:var(--white);width:336px;white-space:nowrap}
.newsletter .field{width:359px;height:36px;background:var(--white);border-radius:5px;display:flex;align-items:center;justify-content:space-between;padding:0 12px;font-size:12.5px;color:#333}
.newsletter .btn{margin-left:10px;width:158px;height:36px;line-height:36px;font-size:15px}

/* section titles */
.section-title{text-align:center;font-family:"Playfair Display",serif;font-weight:400;color:var(--navy);font-size:30px}
.section-title strong{font-weight:700}
.section-title::after{content:"";display:block;width:470px;height:1px;margin:8px auto 0;background:linear-gradient(90deg,transparent,#c7ccd4,transparent)}
.section-title.narrow::after{width:180px}
.section-lead{text-align:center;font-size:14px}

.welcome{padding-top:46px;text-align:center}
.welcome p{width:910px;margin:16px auto 0;font-size:14px;line-height:25.5px}
.welcome .btn{margin-top:16px;width:115px;height:37px;line-height:37px;font-size:13px;font-weight:700}

.services{padding-top:26px}
.services .section-lead{margin-top:12px}
.services-grid{display:flex;justify-content:space-between;width:978px;margin:38px auto 0}
.services .photo{width:475px;height:307px;background:linear-gradient(135deg,#8c7a64,#b8ad96 45%,#5e6a4a 75%,#2d3230)}
.accordion{width:475px}
.acc-item{margin-bottom:7px}
.acc-head{height:53px;background:var(--acc-head);display:flex;align-items:center;justify-content:space-between;padding:0 20px 0 28px;font-size:19px;font-weight:700;color:#2e3644}
.acc-head span{font-size:20px;font-weight:400}
.acc-body{background:var(--acc-body);padding:16px 28px 18px;font-size:12px;line-height:20.5px;color:var(--muted);text-align:justify}

.projects{padding-top:36px}
.projects .section-lead{margin-top:12px}
.project-row{display:flex;justify-content:space-between;width:978px;margin:0 auto}
.project-row.first{margin-top:36px}
.project-row.second{margin-top:16px}
.tile{position:relative;height:174px;overflow:hidden}
.tile::after{content:"+";position:absolute;right:0;bottom:0;width:34px;height:34px;background:linear-gradient(135deg,transparent 50%,var(--navy-deep) 50%);color:var(--white);font-size:16px;font-weight:700;text-align:right;padding:12px 7px 0 0;line-height:20px}
.t1{width:419px}
.t2{width:322px;background:linear-gradient(160deg,#3c3a36,#1d1c1a 60%,#4a4841)}
.t3{width:215px;background:linear-gradient(180deg,#9fb7d6,#cfc7b5 50%,#6e6658)}
.t4{width:209px;background:linear-gradient(180deg,#c7d2d8,#9b8f6c 55%,#6a7a3c)}
.t5{width:243px;background:linear-gradient(150deg,#b49a7a,#3e3328 60%,#8a7a62)}
.t6{width:264px;background:linear-gradient(160deg,#d8c8a8,#5a4a3c 55%,#2e2a28)}
.t7{width:226px;background:linear-gradient(160deg,#1a1d1c,#3a4a2c 60%,#121414)}
.card{padding:14px 26px 0;color:var(--white);background:linear-gradient(120deg,#1d3b7e,#0c2a6a)}
.card h3{font-size:15px;font-weight:700}
.card .customer{font-size:12px;font-style:italic;margin-top:6px}
.card p{font-size:9.4px;line-height:14.5px;margin-top:7px;text-align:justify;width:365px}

/* clients */
.clients{position:absolute;left:0;top:1962px;width:1200px;height:134px;background:var(--band);display:flex;align-items:center;justify-content:center;gap:54px}
.client{font-size:24px;font-weight:700;color:#222}

/* footer */
.footer{position:absolute;left:0;top:2096px;width:1200px;height:254px;background:var(--navy);color:var(--white)}
.footer .col{position:absolute;top:28px}
.footer .brand{left:113px;width:200px}
.footer .brand .logo{color:var(--white)}
.footer .brand p{margin-top:22px;font-size:12px;line-height:20px}
.footer h4{font-size:15px;font-weight:700;text-transform:uppercase;margin-bottom:16px}
.footer .links{left:345px}
.footer .links li{list-style:none;font-size:13px;margin-bottom:10px;display:flex;align-items:center;gap:12px}
.footer .contact{left:490px;width:480px}
.offices{display:flex;gap:14px}
.office{width:150px;font-size:11px;line-height:15px}
.office h5{font-size:12px;font-weight:700;margin-bottom:5px}
.office .row{display:flex;gap:7px;margin-bottom:5px}
.office .row span{overflow-wrap:anywhere}
.office .row svg{margin-top:2px}
.footer .follow{left:995px;width:190px}
.social{display:flex;gap:14px;margin-bottom:20px}
.social a{display:block;width:14px;height:14px;border-radius:50%;background:var(--white)}
.footer .copy{font-size:11px;line-height:18px}
</style>
</head>
<body>

<div class="topbar">
  <div class="item address">
    <svg class="icon" width="9" height="12" viewBox="0 0 9 12"><path d="M4.5 0A4.5 4.5 0 0 0 0 4.5C0 8 4.5 12 4.5 12S9 8 9 4.5A4.5 4.5 0 0 0 4.5 0zm0 6.3a1.8 1.8 0 1 1 0-3.6 1.8 1.8 0 0 1 0 3.6z" fill="#2f3540"/></svg>
    Kavaklı Mah. Çınar Cad. Merkez Plaza No:48 1. Kat İç Kapı No:A3-05 Şişli/İstanbul/Turkey
  </div>
  <div class="item phone">
    <svg class="icon" width="11" height="11" viewBox="0 0 24 24"><path d="M6.6 10.8a15 15 0 0 0 6.6 6.6l2.2-2.2a1 1 0 0 1 1-.25 11.4 11.4 0 0 0 3.6.6 1 1 0 0 1 1 1V20a1 1 0 0 1-1 1A17 17 0 0 1 3 4a1 1 0 0 1 1-1h3.5a1 1 0 0 1 1 1c0 1.250.2 2.45.6 3.6a1 1 0 0 1-.25 1z" fill="#2f3540"/></svg>
    +902120000461
  </div>
  <div class="item">
    <svg class="icon" width="14" height="11" viewBox="0 0 14 11"><rect x=".6" y=".6" width="12.8" height="9.8" fill="none" stroke="#2f3540" stroke-width="1.2"/><path d="M.6.6 7 6l6.4-5.4" fill="none" stroke="#2f3540" stroke-width="1.2"/></svg>
    info@varkoltd-example.com.tr
  </div>
</div>

<header class="header">
  <div class="logo"><span class="tag">Vibration Solutions</span><span class="name">Varko</span></div>
  <nav class="nav">
    <span class="active">Home</span><span>About</span><span>Projects</span><span>Contact Us</span>
  </nav>
  <div class="flags">
    <svg width="27" height="17" viewBox="0 0 27 17" aria-label="English"><rect width="27" height="17" fill="#26387d"/><path d="M0 0 27 17M27 0 0 17" stroke="#fff" stroke-width="3"/><rect x="11" width="5" height="17" fill="#fff"/><rect y="6" width="27" height="5" fill="#fff"/><rect x="12" width="3" height="17" fill="#d0222f"/><rect y="7" width="27" height="3" fill="#d0222f"/></svg>
    <svg width="27" height="17" viewBox="0 0 27 17" aria-label="Türkçe"><rect width="27" height="17" fill="#e02a2f"/><circle cx="11" cy="8.5" r="4.5" fill="#fff"/><circle cx="12.3" cy="8.5" r="3.6" fill="#e02a2f"/><circle cx="17" cy="8.5" r="1.4" fill="#fff"/></svg>
    <svg width="27" height="17" viewBox="0 0 27 17" aria-label="Ελληνικά"><rect width="27" height="17" fill="#2a5fb0"/><g fill="#fff"><rect y="1.9" width="27" height="1.9"/><rect y="5.7" width="27" height="1.9"/><rect y="9.4" width="27" height="1.9"/><rect y="13.2" width="27" height="1.9"/></g><rect width="10" height="9.4" fill="#2a5fb0"/><rect x="4" width="2" height="9.4" fill="#fff"/><rect y="3.7" width="10" height="2" fill="#fff"/></svg>
  </div>
  <svg class="search" width="13" height="13" viewBox="0 0 13 13"><circle cx="5.3" cy="5.3" r="4.2" fill="none" stroke="#222" stroke-width="2"/><path d="M8.4 8.4 12 12" stroke="#222" stroke-width="2.2"/></svg>
</header>

<section class="hero">
  <div class="photo" role="img" aria-label="Photo of smiling engineers in hard hats on a construction site"></div>
  <h1>VARKO ENGINEERING LTD</h1>
  <div class="sub">Vibration Solutions</div>
  <span class="btn">Get Started</span>
  <div class="arrows">
    <span class="arrow"><svg width="10" height="16" viewBox="0 0 10 16"><path d="M8 2 2 8l6 6" fill="none" stroke="#222" stroke-width="2"/></svg></span>
    <span class="arrow"><svg width="10" height="16" viewBox="0 0 10 16"><path d="m2 2 6 6-6 6" fill="none" stroke="#222" stroke-width="2"/></svg></span>
  </div>
</section>

<section class="newsletter">
  <h2>Join Our Newsletter</h2>
  <div class="field">Enter Email id
    <svg width="14" height="11" viewBox="0 0 14 11"><rect x=".6" y=".6" width="12.8" height="9.8" fill="none" stroke="#333" stroke-width="1.2"/><path d="M.6.6 7 6l6.4-5.4" fill="none" stroke="#333" stroke-width="1.2"/></svg>
  </div>
  <span class="btn">Subscribe</span>
</section>

<section class="welcome">
  <h2 class="section-title">Welcome To <strong>Varko Engineering</strong></h2>
  <p>Varko Engineering Ltd. is an engineering company that has been established to provide engineering solutions to industry by employing high-level engineering know-how. The company is specialized in earthquake engineering and vibration solutions in general. Anti-seismic solutions, wind engineering, risk studies, seismic hazard studies and other types of vibration-related issues that have potential to affect structures fit the profile of the company.</p>
  <span class="btn">Read More</span>
</section>

<section class="services">
  <h2 class="section-title narrow">Our <strong>Services</strong></h2>
  <p class="section-lead">Varko Engineering provides cutting-edge solutions to industry in vibration engineering by applying R&amp;D in real-life.</p>
  <div class="services-grid">
    <div class="photo" role="img" aria-label="Photo of an engineer in a hard hat and safety vest operating monitoring equipment on a laptop"></div>
    <div class="accordion">
      <div class="acc-item">
        <div class="acc-head">Structural Sensing and Monitoring <span>–</span></div>
        <div class="acc-body">Varko Engineering Ltd. is expert in structural monitoring and sensing. The company provides solutions for damage assessment, health monitoring or system identification in structural engineering. These solutions can be useful in tall structures, historical monuments, bridges, industrial structures, or wind turbines.</div>
      </div>
      <div class="acc-item"><div class="acc-head">Wind Engineering Studies <span>+</span></div></div>
      <div class="acc-item"><div class="acc-head">Seismic Risk Studies <span>+</span></div></div>
    </div>
  </div>
</section>

<section class="projects">
  <h2 class="section-title narrow">Our <strong>Projects</strong></h2>
  <p class="section-lead">Sample Projects in Vibration Solutions</p>
  <div class="project-row first">
    <div class="tile t1 card">
      <h3>Seismic Monitoring Consultancy</h3>
      <div class="customer">Customer: Kestrel Strait Tunnel</div>
      <p>Varko Engineering Ltd is awarded for consultancy for seismic monitoring of Istanbul's prestige project, Strait Crossing Tunnel. Varko Engineering – Vibration Solutions will be responsible with the improvement, operation and data collection of the tunnel monitoring system, installed by Telvane Systems, as well as development of criteria for seismic after-event actions to be taken.</p>
    </div>
    <div class="tile t2" role="img" aria-label="Photo of sensor equipment placed inside a tunnel at night"></div>
    <div class="tile t3" role="img" aria-label="Photo of a historic building facade under assessment"></div>
  </div>
  <div class="project-row second">
    <div class="tile t4" role="img" aria-label="Photo of a stone church monument on a hillside"></div>
    <div class="tile t5" role="img" aria-label="Photo of cabling and sensors installed on a structure"></div>
    <div class="tile t6" role="img" aria-label="Photo of a laptop showing vibration data on site"></div>
    <div class="tile t7" role="img" aria-label="Photo of a technician in a safety vest installing a sensor"></div>
  </div>
</section>

<section class="clients">
  <span class="client">Pruvane</span>
  <span class="client">Quillnet</span>
  <span class="client">Solmere Financial</span>
  <span class="client">Swivo</span>
  <span class="client">Lintara</span>
  <span class="client">Yarrow</span>
</section>

<footer class="footer">
  <div class="col brand">
    <div class="logo"><span class="tag">Vibration Solutions</span><span class="name">Varko</span></div>
    <p>Nemo enim ipsam voluptatem quia voluptas sit aspernatur aut odit aut fugit, sed quia consequuntur magni dolores eos</p>
  </div>
  <div class="col links">
    <h4>Quick Links</h4>
    <ul>
      <li><svg width="6" height="9" viewBox="0 0 6 9"><path d="m1 1 3.5 3.5L1 8" fill="none" stroke="#fff" stroke-width="1.3"/></svg>Home</li>
      <li><svg width="6" height="9" viewBox="0 0 6 9"><path d="m1 1 3.5 3.5L1 8" fill="none" stroke="#fff" stroke-width="1.3"/></svg>About</li>
      <li><svg width="6" height="9" viewBox="0 0 6 9"><path d="m1 1 3.5 3.5L1 8" fill="none" stroke="#fff" stroke-width="1.3"/></svg>Projects</li>
      <li><svg width="6" height="9" viewBox="0 0 6 9"><path d="m1 1 3.5 3.5L1 8" fill="none" stroke="#fff" stroke-width="1.3"/></svg>Contact Us</li>
    </ul>
  </div>
  <div class="col contact">
    <h4>Contact Info</h4>
    <div class="offices">
      <div class="office">
        <h5>Turkey</h5>
        <div class="row"><svg width="8" height="11" viewBox="0 0 9 12"><path d="M4.5 0A4.5 4.5 0 0 0 0 4.5C0 8 4.5 12 4.5 12S9 8 9 4.5A4.5 4.5 0 0 0 4.5 0zm0 6.3a1.8 1.8 0 1 1 0-3.6 1.8 1.8 0 0 1 0 3.6z" fill="#fff"/></svg><span>Kavaklı Mah. Çınar Cad. Merkez Plaza No:48 1. Kat İç Kapı No:A3-05 Şişli/İstanbul/Turkey</span></div>
        <div class="row"><svg width="10" height="10" viewBox="0 0 24 24"><path d="M6.6 10.8a15 15 0 0 0 6.6 6.6l2.2-2.2a1 1 0 0 1 1-.25 11.4 11.4 0 0 0 3.6.6 1 1 0 0 1 1 1V20a1 1 0 0 1-1 1A17 17 0 0 1 3 4a1 1 0 0 1 1-1h3.5a1 1 0 0 1 1 1c0 1.25.2 2.45.6 3.6a1 1 0 0 1-.25 1z" fill="#fff"/></svg><span>+902120000461</span></div>
        <div class="row"><svg width="11" height="9" viewBox="0 0 14 11"><rect x=".6" y=".6" width="12.8" height="9.8" fill="none" stroke="#fff" stroke-width="1.2"/><path d="M.6.6 7 6l6.4-5.4" fill="none" stroke="#fff" stroke-width="1.2"/></svg><span>info@varkoltd-example.com.tr</span></div>
      </div>
      <div class="office">
        <h5>The Netherlands</h5>
        <div class="row"><svg width="8" height="11" viewBox="0 0 9 12"><path d="M4.5 0A4.5 4.5 0 0 0 0 4.5C0 8 4.5 12 4.5 12S9 8 9 4.5A4.5 4.5 0 0 0 4.5 0zm0 6.3a1.8 1.8 0 1 1 0-3.6 1.8 1.8 0 0 1 0 3.6z" fill="#fff"/></svg><span>Varko Engineering B.V.<br>Lindehof 52, 9714TK, Oostbroek, The Netherlands</span></div>
        <div class="row"><svg width="10" height="10" viewBox="0 0 24 24"><path d="M6.6 10.8a15 15 0 0 0 6.6 6.6l2.2-2.2a1 1 0 0 1 1-.25 11.4 11.4 0 0 0 3.6.6 1 1 0 0 1 1 1V20a1 1 0 0 1-1 1A17 17 0 0 1 3 4a1 1 0 0 1 1-1h3.5a1 1 0 0 1 1 1c0 1.25.2 2.45.6 3.6a1 1 0 0 1-.25 1z" fill="#fff"/></svg><span>+31 (0)6 00 00 73 85</span></div>
        <div class="row"><svg width="11" height="9" viewBox="0 0 14 11"><rect x=".6" y=".6" width="12.8" height="9.8" fill="none" stroke="#fff" stroke-width="1.2"/><path d="M.6.6 7 6l6.4-5.4" fill="none" stroke="#fff" stroke-width="1.2"/></svg><span>info@varkoengineering-example.com</span></div>
      </div>
      <div class="office">
        <h5>Greece</h5>
        <div class="row"><svg width="8" height="11" viewBox="0 0 9 12"><path d="M4.5 0A4.5 4.5 0 0 0 0 4.5C0 8 4.5 12 4.5 12S9 8 9 4.5A4.5 4.5 0 0 0 4.5 0zm0 6.3a1.8 1.8 0 1 1 0-3.6 1.8 1.8 0 0 1 0 3.6z" fill="#fff"/></svg><span>Leof. Trigonou 7 &amp; Paronos<br>Ano Kalyvia, 14590<br>Athens, Greece</span></div>
        <div class="row"><svg width="10" height="10" viewBox="0 0 24 24"><path d="M6.6 10.8a15 15 0 0 0 6.6 6.6l2.2-2.2a1 1 0 0 1 1-.25 11.4 11.4 0 0 0 3.6.6 1 1 0 0 1 1 1V20a1 1 0 0 1-1 1A17 17 0 0 1 3 4a1 1 0 0 1 1-1h3.5a1 1 0 0 1 1 1c0 1.25.2 2.45.6 3.6a1 1 0 0 1-.25 1z" fill="#fff"/></svg><span>+30 210 0000947</span></div>
      </div>
    </div>
  </div>
  <div class="col follow">
    <h4>Follow Us</h4>
    <div class="social">
      <a href="https://www.facebook.com/varkoengineering/" aria-label="Facebook"></a>
      <a href="https://twitter.com/VarkoEng" aria-label="Twitter"></a>
      <a href="https://www.linkedin.com/in/varko-mühendislik-x7q20419/" aria-label="LinkedIn"></a>
    </div>
    <div class="copy">Copyright© 2018. Company Name<br>All Right Reserved</div>
  </div>
</footer>

</body>
</html>
```